Health - Still Meadow Project

I am running a new Still Meadow Conference that will have meditation, mediums and healers - this is a first time conference. However the conference is aimed at mainstream 'normal' people. The 'normal' people, don't want to hear or see words like Tantra, Prana, Angels, etc, but they have problems that can be alleviated through these mediums. The design should communicate light, soothing, comforting, healing. I would like a web design for a single page that can be used as a landing page for the conference registration. I also need a logo and a flyer that can be made into posters A4 or A3 posters. I need to be able to edit all documents as there will be changes in the program through time. I have attached the initial agenda. This conference will be held in Victoria, Australia.
Target Market(s)
Mums and grandmas
Industry/Entity Type
Health And Wellness
Number of Pages Required
1 page

```html
<!DOCTYPE html>
<html lang="en">
<head>
<meta charset="utf-8">
<title>Still Meadow Conference – Register</title>
<link href="https://fonts.googleapis.com/css2?family=Gelasio:wght@400;700&family=Open+Sans:wght@400;600;700&display=swap" rel="stylesheet">
<style>
:root{
  --blue:#1e95dc;
  --blue-dark:#1378c2;
  --ink:#3d4248;
  --muted:#6b7178;
  --line:#dcdfe3;
  --soft:#eef0f2;
  --night:#1d2630;
  --footer:#2a3039;
  --footer-deep:#20252c;
  --white:#ffffff;
}
*{box-sizing:border-box;margin:0;padding:0}
html,body{width:1200px;height:3796px;overflow:hidden}
body{font-family:"Open Sans",Arial,sans-serif;color:var(--ink);background:var(--white);font-size:14px;line-height:1.6}
.serif{font-family:"Gelasio",Georgia,serif}
.btn{display:inline-block;background:var(--blue);color:var(--white);font-size:15px;font-weight:600;padding:10px 26px;border-radius:3px;letter-spacing:.2px}

/* hero */
.hero{position:relative;height:560px;background:linear-gradient(180deg,#2a3a50 0%,#4d5a70 30%,#b38a62 58%,#d89a5a 66%,#5a5a62 78%,#1f2630 100%);color:var(--white);text-align:center}
.hero-photo{position:absolute;inset:0}
.topbar{position:absolute;top:0;left:0;right:0;height:70px;display:flex;align-items:center;justify-content:space-between;padding:0 70px 0 80px;background:rgba(10,20,35,.35)}
.brand{display:flex;align-items:center;gap:10px;font-family:"Gelasio",Georgia,serif;font-size:24px;color:var(--white)}
.brand-dot{width:30px;height:30px;border-radius:50%;background:var(--blue)}
.contact-top{display:flex;gap:40px;font-size:14px}
.contact-top span{display:flex;align-items:center;gap:8px}
.hero h1{position:relative;padding-top:220px;font-family:"Gelasio",Georgia,serif;font-weight:400;font-size:50px;line-height:1.15;text-shadow:0 2px 8px rgba(0,0,0,.4)}
.hero .btn{position:relative;margin-top:40px}

/* intro */
.intro{height:370px;position:relative;padding:50px 0 0 110px}
.intro-text{width:700px}
.intro h2{font-family:"Gelasio",Georgia,serif;font-weight:700;color:var(--blue);font-size:34px;line-height:1.1}
.intro .date{font-family:"Gelasio",Georgia,serif;font-size:22px;color:var(--ink);margin:4px 0 22px}
.intro p{font-size:13px;color:var(--muted);margin-bottom:14px;line-height:1.55}
.intro-photo{position:absolute;right:70px;top:20px;width:330px;height:330px;background:linear-gradient(160deg,#eaf4fb 0%,#c4e1f5 55%,#7fb3d8 100%)}

/* bands */
.band{position:relative;color:var(--white);text-align:center}
.band-city{height:370px;background:linear-gradient(180deg,#1a2331 0%,#2c3b52 45%,#35506a 70%,#151c26 100%);padding-top:82px}
.band-city .kicker{font-family:"Gelasio",Georgia,serif;font-size:31px}
.band-city .big{font-family:"Gelasio",Georgia,serif;font-size:44px;color:#3aa9ec;line-height:1.25;margin-top:8px}
.band-city .sub{font-family:"Gelasio",Georgia,serif;font-size:31px;line-height:1.2}
.band .btn{margin-top:28px}
.band-coast{height:380px;background:linear-gradient(180deg,#1b2a3a 0%,#2f4a66 40%,#4a6c86 62%,#1a2430 100%);padding-top:92px}
.band-coast h3{font-family:"Gelasio",Georgia,serif;font-weight:400;font-size:44px;color:#3aa9ec;line-height:1.2}
.band-coast .sub{font-family:"Gelasio",Georgia,serif;font-size:34px;line-height:1.25}

/* sessions */
.sessions{display:flex;justify-content:center;gap:50px}
.sessions-a{height:940px;padding-top:50px}
.sessions-b{height:820px;padding-top:40px}
.card{width:450px;border:1px solid var(--line);background:var(--white);padding:40px 30px 0;position:relative;text-align:center}
.sessions-a .card{height:850px}
.sessions-b .card{height:740px}
.portrait{width:190px;height:190px;border-radius:50%;margin:0 auto 24px;border:4px solid var(--white);box-shadow:0 0 0 1px var(--line)}
.tone-a{background:radial-gradient(circle at 50% 40%,#d9a88a,#7a4a3a 70%,#3d8fb0)}
.tone-b{background:radial-gradient(circle at 50% 45%,#e0b894,#a0643c 70%,#eadbc6)}
.tone-c{background:radial-gradient(circle at 50% 45%,#d8b39a,#8a6a58 70%,#5a5040)}
.tone-d{background:radial-gradient(circle at 50% 45%,#c89a7c,#5a4a40 70%,#7aa0b4)}
.card h4{font-family:"Gelasio",Georgia,serif;font-weight:400;color:var(--blue);font-size:22px;line-height:1.3;margin-bottom:18px}
.card p{font-size:12.5px;color:var(--muted);text-align:left;margin-bottom:12px;line-height:1.6}
.facilitator{position:absolute;left:30px;right:30px;bottom:30px;background:var(--soft);border:1px solid var(--line);font-size:13px;color:var(--muted);padding:10px 14px}

/* footer */
.footer{height:316px;background:var(--footer);color:#c9ced4;display:flex;justify-content:space-between;padding:40px 110px 0 110px}
.footer h5{font-family:"Gelasio",Georgia,serif;font-weight:400;color:#3aa9ec;font-size:26px;margin-bottom:12px;border-bottom:1px solid #454c56;padding-bottom:8px}
.register{width:640px}
.fields{display:grid;grid-template-columns:1fr 1fr;gap:6px 30px}
.field label{display:block;font-size:12px;color:#c9ced4}
.field .input{height:28px;border-bottom:1px solid #555c66}
.field.wide{grid-column:1 / span 2}
.register .btn{margin-top:14px;padding:7px 30px;font-size:14px}
.contact{width:300px}
.contact-row{display:flex;gap:10px;font-size:13px;margin-bottom:8px;align-items:flex-start}
.socials{display:flex;gap:8px;margin-top:14px}
.socials span{width:30px;height:30px;background:var(--blue-dark);border-radius:3px}
.copyright{height:40px;background:var(--footer-deep);color:#8a9099;font-size:12px;text-align:center;line-height:40px}
</style>
</head>
<body>

<header class="hero">
  <div class="hero-photo" role="img" aria-label="Photo of a person meditating by the sea at sunset"></div>
  <div class="topbar">
    <div class="brand"><span class="brand-dot"></span>Still Meadow</div>
    <div class="contact-top">
      <span><svg width="14" height="14" viewBox="0 0 24 24" fill="#fff"><path d="M6.6 10.8a15 15 0 0 0 6.6 6.6l2.2-2.2c.3-.3.7-.4 1-.2 1.1.4 2.3.6 3.6.6.6 0 1 .4 1 1V20c0 .6-.4 1-1 1A17 17 0 0 1 3 4c0-.6.4-1 1-1h3.5c.6 0 1 .4 1 1 0 1.3.2 2.5.6 3.6.1.3 0 .7-.2 1z"/></svg>Call Us: 555-0142-7730</span>
      <span><svg width="15" height="12" viewBox="0 0 24 18" fill="#fff"><path d="M0 0h24v18H0z" fill="none"/><path d="M1 1h22v16H1z" fill="none" stroke="#fff" stroke-width="2"/><path d="M1 1l11 9 11-9" fill="none" stroke="#fff" stroke-width="2"/></svg>Email: hello@stillmeadow.org</span>
    </div>
  </div>
  <h1>Experience an<br>Awakening Discover HOPE!</h1>
  <a class="btn">Register Now!</a>
</header>

<section class="intro">
  <div class="intro-text">
    <h2>Still Meadow Conference</h2>
    <div class="date">Saturday August 20th 2016</div>
    <p>Join us for a gentle, welcoming day designed for everyday people who want to feel calmer, lighter and more hopeful. Through guided meditation, honest conversation and caring healers, you will learn simple ways to ease stress, release old worries and reconnect with what matters most. No experience is needed and there is nothing strange to learn, just a quiet space to rest, listen and begin again. Bring a friend, your mother or your daughter and share a day of comfort together in the beautiful Victorian countryside.</p>
    <p>Every session is led by warm, experienced facilitators who understand real life, family pressures and the need for practical care. You will leave with easy tools you can use at home.</p>
  </div>
  <div class="intro-photo" role="img" aria-label="Photo of a smiling woman raising her arms against a bright sky"></div>
</section>

<section class="band band-city" role="img" aria-label="Night view of a city skyline over water">
  <div class="kicker">Discover Hope Start Your Recovery Today</div>
  <div class="big">Meditation, Mediums &amp; Healers.</div>
  <div class="sub">Help you solved your problems</div>
  <a class="btn">Register Now!</a>
</section>

<section class="sessions sessions-a">
  <article class="card">
    <div class="portrait tone-a" role="img" aria-label="Portrait photo of the session facilitator"></div>
    <h4>Wild Hares – Embarking Upon<br>the Spiritual Life</h4>
    <p>Everyone is searching for love, joy and peace, and yet the busy pace of daily life so often pulls us away from the calm we long for. In this session we gently explore how small daily habits can open the door to a fuller, kinder and more settled way of living. You will be invited to pause, breathe and notice what is really asking for your attention.</p>
    <p>It could take an entire lifetime of study to fully grasp the magnitude of this kind of awakening. In this session you will receive a very simple, friendly understanding of the journey toward inner peace, from confusion to clarity, and practical steps you can take right away.</p>
    <p>Whether you are new to this path or returning after many years, you will find a warm welcome, plain language and a room full of people just like you.</p>
    <div class="facilitator">Facilitator: Maren Holt &nbsp;&nbsp;|&nbsp;&nbsp; (10:00am – 11:45am)</div>
  </article>
  <article class="card">
    <div class="portrait tone-b" role="img" aria-label="Portrait photo of the session facilitator"></div>
    <h4>Conscious Connection &amp;<br>Living Life Fully</h4>
    <p>We live in a world where most people feel disconnected or out of sync with friends, loved ones and the daily experience we share with one another. This workshop is designed to offer you a framework to feel more connected, more present and more at ease with the people around you and with yourself.</p>
    <p>The more we feel connected to ourselves, the more connected we will feel with others. In a time where more and more people are feeling isolated, this gentle practice can restore a sense of belonging, connection and fulfilment. Come and explore simple, welcoming exercises that deepen a heartfelt, authentic and healing space.</p>
    <p>You will leave with easy tools for listening well, speaking kindly and bringing more warmth into every relationship you hold dear.</p>
    <div class="facilitator">Facilitator: Ada Quinn &nbsp;&nbsp;|&nbsp;&nbsp; (11:00am – 12:45pm)</div>
  </article>
</section>

<section class="band band-coast" role="img" aria-label="Coastal city waterfront at dusk">
  <h3>Achieve Your Recovery And Sobriety In Paradise</h3>
  <div class="sub">Conference Will Be Held In Australia</div>
  <a class="btn">Register Now!</a>
</section>

<section class="sessions sessions-b">
  <article class="card">
    <div class="portrait tone-c" role="img" aria-label="Portrait photo of the session facilitator"></div>
    <h4>The Slow Breath to Freedom</h4>
    <p>Stress is one of the main causes of lasting illness today. This session combines breath and body awareness to help you slow down, ease tension and find rest. Through simple breathing exercises, mindfulness and quiet reflection you will discover how easily calm can return.</p>
    <p>Using his highly intuitive skills and the gentle breathing process, our facilitator will help you experience your deeper nature and transform your individual power, enabling you to live with more harmony and peace.</p>
    <div class="facilitator">Facilitator: Tom Reyes &nbsp;&nbsp;|&nbsp;&nbsp; (1:00pm – 3:15pm)</div>
  </article>
  <article class="card">
    <div class="portrait tone-d" role="img" aria-label="Portrait photo of the session facilitator"></div>
    <h4>Learning to SHINE</h4>
    <p>In a world where we often feel less than our bright, shiny best, we are all affected by the outer voices of our own doubt and fear. In this session we will gently move through ways to reconnect with your inner light, rediscover your natural joy and let it shine into everyday life.</p>
    <p>You will be guided through simple, caring practices that bring warmth and confidence, so that you leave feeling lighter, brighter and ready to share your glow with those you love.</p>
    <div class="facilitator">Facilitator: Iris Wells &nbsp;&nbsp;|&nbsp;&nbsp; (3:15pm – 5:00pm)</div>
  </article>
</section>

<footer class="footer">
  <div class="register">
    <h5>Register Now</h5>
    <div class="fields">
      <div class="field"><label>First Name</label><div class="input"></div></div>
      <div class="field"><label>Last Name</label><div class="input"></div></div>
      <div class="field"><label>E-mail</label><div class="input"></div></div>
      <div class="field"><label>Phone</label><div class="input"></div></div>
      <div class="field wide"><label>Your Message</label><div class="input"></div></div>
    </div>
    <a class="btn">Submit</a>
  </div>
  <div class="contact">
    <h5>Contact us</h5>
    <div class="contact-row"><svg width="12" height="16" viewBox="0 0 12 16"><path d="M6 0a6 6 0 0 0-6 6c0 4.5 6 10 6 10s6-5.5 6-10a6 6 0 0 0-6-6zm0 8.5A2.5 2.5 0 1 1 6 3.5a2.5 2.5 0 0 1 0 5z" fill="#3aa9ec"/></svg><span>12 Meadow Lane, Daylesford<br>Victoria 3460 Australia</span></div>
    <div class="contact-row"><svg width="14" height="14" viewBox="0 0 24 24" fill="#3aa9ec"><path d="M6.6 10.8a15 15 0 0 0 6.6 6.6l2.2-2.2c.3-.3.7-.4 1-.2 1.1.4 2.3.6 3.6.6.6 0 1 .4 1 1V20c0 .6-.4 1-1 1A17 17 0 0 1 3 4c0-.6.4-1 1-1h3.5c.6 0 1 .4 1 1 0 1.3.2 2.5.6 3.6.1.3 0 .7-.2 1z"/></svg><span>Phone: +61 3 5550 1187</span></div>
    <div class="contact-row"><svg width="14" height="11" viewBox="0 0 24 18"><path d="M1 1h22v16H1z" fill="none" stroke="#3aa9ec" stroke-width="2"/><path d="M1 1l11 9 11-9" fill="none" stroke="#3aa9ec" stroke-width="2"/></svg><span>hello@stillmeadow.org</span></div>
    <div class="socials"><span></span><span></span><span></span><span></span><span></span></div>
  </div>
</footer>
<div class="copyright">Copyright © 2016 Still Meadow, All Rights Reserved</div>

</body>
</html>
```